Upscale business cards needed for family business

We need professional business cards created for several family members. We are a family business holding company. We would like these relatively simple and straightforward, but also with a unique element to set them apart. Probably stick with neutral and simple colors - white, grey etc. We need space for the traditional elements, including name, title, address, email/phone number. And we will be creating several from this template so it needs to be template that is easy to switch information in and out of.

Industry/Entity Type

Business

Contact Information for Business Card

Please include the attached Dunmore Ventures logo.

Requirements
Must have
• The attached Dunmore Ventures logo.

```html
<!DOCTYPE html>
<html lang="en">
<head>
<meta charset="UTF-8">
<title>Dunmore Ventures – Business Card</title>
<link href="https://fonts.googleapis.com/css2?family=Zilla+Slab:ital,wght@0,300;1,300&display=swap" rel="stylesheet">
<style>
  :root {
    --page-bg: #e9e4df;
    --card-black: #0b0b0b;
    --card-deep: #181818;
    --gold: #d9a935;
    --gold-soft: #b8892a;
  }
  * { box-sizing: border-box; margin: 0; padding: 0; }
  html, body {
    width: 1200px; height: 900px; overflow: hidden;
    background: var(--page-bg);
    font-family: "Zilla Slab", "Rockwell", serif;
    font-weight: 300;
  }
  .stage {
    width: 1200px; height: 900px;
    display: flex; align-items: center; justify-content: center;
  }
  .business-card {
    position: relative;
    width: 840px; height: 480px;
    background: var(--card-black);
    overflow: hidden;
    box-shadow: 0 10px 30px rgba(0,0,0,0.25);
  }
  .card-texture {
    position: absolute; inset: 0;
    background: radial-gradient(ellipse at 45% 40%, var(--card-deep) 0%, var(--card-black) 70%);
  }
  .card-frame {
    position: absolute;
    left: 40px; top: 38px; right: 40px; bottom: 40px;
    border: 2px solid var(--gold-soft);
  }
  .company-name {
    position: absolute; top: 92px; left: 0; right: 0;
    text-align: center;
    color: var(--gold);
    font-weight: 300;
    font-size: 28px;
    letter-spacing: 1.5px;
    text-transform: uppercase;
    line-height: 1;
  }
  .company-name .suffix { display: block; font-size: 14px; letter-spacing: 2px; margin-top: 4px; }
  .person {
    position: absolute; left: 70px; top: 262px;
    color: var(--gold);
  }
  .person-name { font-size: 23px; }
  .person-title { font-size: 19px; font-style: italic; margin-top: 4px; }
  .divider {
    position: absolute; left: 372px; top: 192px;
    width: 1px; height: 130px; background: var(--gold-soft);
  }
  .contact-list {
    position: absolute; left: 392px; top: 188px;
    list-style: none; color: var(--gold); font-size: 19px; line-height: 1.15;
  }
  .contact-list li { display: flex; align-items: flex-start; gap: 12px; margin-bottom: 6px; }
  .contact-list svg { flex: none; width: 20px; height: 20px; margin-top: 1px; }
  .website {
    position: absolute; bottom: 29px; left: 0; right: 0;
    text-align: center;
  }
  .website span {
    display: inline-block;
    background: var(--card-black);
    padding: 0 14px;
    color: var(--gold);
    font-size: 18px;
    letter-spacing: 4px;
  }
</style>
</head>
<body>
<main class="stage">
  <article class="business-card">
    <div class="card-texture" role="img" aria-label="Subtle dark geometric block pattern across the card background"></div>
    <div class="card-frame"></div>

    <h1 class="company-name">Dunmore Ventures<span class="suffix">Inc</span></h1>

    <div class="person">
      <p class="person-name">FirstName Last Name</p>
      <p class="person-title">Position</p>
    </div>

    <div class="divider"></div>

    <ul class="contact-list">
      <li>
        <svg viewBox="0 0 20 20"><circle cx="10" cy="10" r="10" fill="var(--gold)"/><path d="M10 4a3.5 3.5 0 0 0-3.5 3.5C6.5 10 10 15 10 15s3.5-5 3.5-7.5A3.5 3.5 0 0 0 10 4z" fill="#0b0b0b"/><circle cx="10" cy="7.5" r="1.3" fill="var(--gold)"/></svg>
        <span>000 Any Place Drive, South Field,<br>QK 042217</span>
      </li>
      <li>
        <svg viewBox="0 0 20 20"><circle cx="10" cy="10" r="10" fill="var(--gold)"/><path d="M6.5 5l2 2-1 1.5c.8 1.6 2 2.8 3.5 3.5l1.5-1 2 2-1.3 1.5C9.5 14 6 10.5 5 6.3z" fill="#0b0b0b"/></svg>
        <span>+1 555 014 2368</span>
      </li>
      <li>
        <svg viewBox="0 0 20 20"><circle cx="10" cy="10" r="10" fill="var(--gold)"/><rect x="6.8" y="4.5" width="6.4" height="11" rx="1" fill="#0b0b0b"/><rect x="7.8" y="6" width="4.4" height="7" fill="var(--gold)"/></svg>
        <span>+1 555 019 7745</span>
      </li>
      <li>
        <svg viewBox="0 0 20 20"><circle cx="10" cy="10" r="10" fill="var(--gold)"/><rect x="5" y="6.5" width="10" height="7" fill="#0b0b0b"/><path d="M5 6.5l5 4 5-4" fill="none" stroke="var(--gold)" stroke-width="1"/></svg>
        <span>mail@dunmore.com</span>
      </li>
    </ul>

    <p class="website"><span>www.dunmoreventuresinc.com</span></p>
  </article>
</main>
</body>
</html>
```